10-year customer thank you card

We want a greeting card that our sales reps can send to companies/customers who have been with our company for 10 or more years. We're a software company, our corporate color is blue but we also like green, orange, and purple. We'd like something rather minimal/simplistic for this card, perhaps building off our tree logo. We're really open to ideas for this one. You must use the template files that are uploaded. Copy included in 10 year thank you card file; the copy may change based on how it looks when laid out
Updates

I updated our brief. We'd prefer a sans serif font. I also uploaded a blank infographic image that includes more of our approved colors.

Industry/Entity Type

Software

Font styles to use
Sans Serif

```html
<!DOCTYPE html>
<html lang="en">
<head>
<meta charset="utf-8">
<title>Larchfield Software – 10 Years Thank You Card</title>
<link rel="stylesheet" href="https://fonts.googleapis.com/css2?family=Raleway:wght@300;400;500&display=swap">
<style>
  :root {
    --orange: #f7931e;
    --orange-deep: #fc4f0c;
    --orange-mid: #fb7a12;
    --orange-light: #fb9a1c;
    --ink: #2b2b2b;
    --rule: #3a3a3a;
    --paper: #ffffff;
    --years: #f26a1b;
  }
  * { margin: 0; padding: 0; box-sizing: border-box; }
  html, body {
    width: 869px;
    height: 1200px;
    overflow: hidden;
    background: var(--paper);
  }
  .card {
    position: relative;
    width: 869px;
    height: 1200px;
    background: var(--paper);
    overflow: hidden;
    font-family: "Raleway", Arial, sans-serif;
  }

  /* Back panel: printed upside down so it reads correctly once folded */
  .back-header {
    position: absolute;
    left: 0;
    top: 0;
    width: 869px;
    height: 73px;
    transform: rotate(180deg);
  }
  .back-header__bar {
    position: absolute;
    left: 41px;
    right: 42px;
    bottom: 0;
    height: 7px;
    background: var(--orange);
  }
  .back-header__rule {
    position: absolute;
    left: 41px;
    right: 42px;
    top: 0;
    height: 2px;
    background: var(--rule);
  }
  .back-header__brand {
    position: absolute;
    left: 42px;
    top: 20px;
    display: flex;
    align-items: center;
    gap: 8px;
    font-weight: 500;
    font-size: 20px;
    color: var(--ink);
  }
  .back-header__brand-mark {
    width: 14px;
    height: 14px;
    background: var(--orange-deep);
  }
  .back-header__web {
    position: absolute;
    right: 42px;
    top: 22px;
    font-weight: 500;
    font-size: 16px;
    color: var(--orange-deep);
    letter-spacing: 0.3px;
  }

  /* Front panel */
  .front {
    position: absolute;
    left: 0;
    top: 599px;
    width: 869px;
    height: 601px;
    background: linear-gradient(180deg, var(--orange-light) 0%, var(--orange-mid) 55%, var(--orange-deep) 100%);
  }
  .front__waves {
    position: absolute;
    inset: 0;
  }
  .front__years {
    position: absolute;
    left: 40px;
    top: 44px;
    font-weight: 300;
    font-size: 74px;
    letter-spacing: -2px;
    color: var(--years);
    line-height: 1;
  }
  .front__brand {
    position: absolute;
    left: 0;
    width: 869px;
    top: 118px;
    display: flex;
    flex-direction: column;
    align-items: center;
    gap: 22px;
  }
  .front__brand-mark {
    width: 150px;
    height: 150px;
    background: var(--paper);
  }
  .front__brand-name {
    font-weight: 500;
    font-size: 46px;
    color: var(--paper);
    line-height: 1;
    letter-spacing: 1px;
  }
  .front__thanks {
    position: absolute;
    left: 0;
    width: 869px;
    top: 432px;
    text-align: center;
    font-weight: 300;
    font-size: 92px;
    color: var(--paper);
    line-height: 1;
    letter-spacing: 1px;
  }
</style>
</head>
<body>
<main class="card">
  <header class="back-header">
    <div class="back-header__rule"></div>
    <div class="back-header__brand"><span class="back-header__brand-mark"></span>Larchfield Software</div>
    <div class="back-header__web">www.larchfield.com</div>
    <div class="back-header__bar"></div>
  </header>

  <section class="front">
    <svg class="front__waves" width="869" height="601" viewBox="0 0 869 601" aria-hidden="true">
      <path d="M0 60 C200 120 420 140 600 110 C720 90 800 70 869 60 L869 0 L0 0 Z" fill="#fca21f" opacity="0.5"/>
      <path d="M0 240 C180 200 360 230 520 300 C650 360 760 330 869 280 L869 601 L0 601 Z" fill="#fb7d10" opacity="0.55"/>
      <path d="M0 340 C160 300 320 340 470 390 C620 440 760 400 869 370 L869 601 L0 601 Z" fill="#fc6a0e" opacity="0.5"/>
      <path d="M0 470 C200 430 420 470 600 500 C720 520 800 500 869 480 L869 601 L0 601 Z" fill="#fd540b" opacity="0.6"/>
    </svg>
    <div class="front__years">10 years</div>
    <div class="front__brand">
      <span class="front__brand-mark"></span>
      <span class="front__brand-name">Larchfield</span>
    </div>
    <div class="front__thanks">Thank You</div>
  </section>
</main>
</body>
</html>
```